依頼概要
■依頼の目的/概要
当方、眼鏡店です。7年以上ご来店が無い75歳以上の顧客様に、来店を促すDMを考えております。

■依頼詳細
枚数:約250枚
サイズ:はがきサイズ

■要望
・眼鏡店だとわかりやすいイラストをお願いします。
・添付ファイルの文面を入れて下さい。

その他何かご不明な点がございましたら、お気軽にご質問下さい。
よろしくお願いいたします。

・親しみやすいデザイン。
・サービス内容が分かりやすく書かれていた。

皆様からご提案頂き、誠にありがとうございました。
どれも素晴らしいデザイン案でしたので、選考にも大変悩みました。
また依頼させて頂いた際には、よろしくお願いいたします。

```html
<!DOCTYPE html>
<html lang="ja">
<head>
<meta charset="utf-8">
<title>メガネのミハラ 北町店 ご来店のご案内</title>
<link rel="stylesheet" href="https://fonts.googleapis.com/css2?family=Noto+Sans+JP:wght@500;700;900&display=swap">
<style>
  :root {
    --green: #1e8a4c;
    --white: #ffffff;
    --ink: #1f1f1f;
    --paper: #f1f1ee;
    --paper-shade: #c9cbc6;
    --brand-red: #c8242b;
  }
  html, body {
    margin: 0;
    padding: 0;
    overflow: hidden;
    background: var(--white);
  }
  .postcard {
    position: relative;
    width: 809px;
    height: 1200px;
    background: var(--green);
    overflow: hidden;
    font-family: "Noto Sans JP", sans-serif;
    color: var(--white);
  }
  .headline {
    position: absolute;
    left: 34px;
    top: 22px;
    margin: 0;
    font-weight: 900;
    font-size: 64px;
    line-height: 72px;
    letter-spacing: 6px;
  }
  .headline span { display: block; }
  .visual {
    position: absolute;
    left: 0;
    top: 183px;
    width: 809px;
    height: 500px;
    background:
      linear-gradient(180deg, transparent 0 30%, rgba(20,20,20,0.85) 30% 38%, transparent 38% 100%),
      radial-gradient(ellipse at 55% 60%, var(--paper) 0 45%, var(--paper-shade) 80%);
  }
  .message {
    position: absolute;
    left: 46px;
    top: 698px;
    margin: 0;
    font-weight: 500;
    font-size: 35px;
    line-height: 55px;
    letter-spacing: 1px;
  }
  .shop-card {
    position: absolute;
    left: 48px;
    top: 1076px;
    width: 716px;
    height: 112px;
    background: var(--white);
    color: var(--ink);
    display: flex;
    align-items: center;
  }
  .shop-mark {
    width: 240px;
    height: 84px;
    display: flex;
    align-items: center;
    justify-content: center;
    gap: 10px;
    border-right: 2px solid var(--paper-shade);
  }
  .shop-mark .dot {
    width: 18px;
    height: 18px;
    border-radius: 50%;
    background: var(--brand-red);
  }
  .shop-mark .name {
    font-weight: 900;
    font-size: 44px;
    color: var(--brand-red);
    letter-spacing: 2px;
  }
  .shop-info {
    padding-left: 22px;
    font-weight: 700;
    font-size: 25px;
    line-height: 34px;
  }
  .shop-info p { margin: 0; }
  .shop-info .tel { display: flex; align-items: center; gap: 8px; }
</style>
</head>
<body>
  <main class="postcard">
    <h1 class="headline">
      <span>そのメガネ、</span>
      <span>よく見えていますか？</span>
    </h1>

    <div class="visual" role="img" aria-label="新聞の文字をメガネ越しに見たイラスト"></div>

    <p class="message">
      お世話になっております。<br>
      お使いの眼鏡の具合はいかがでしょうか。<br>
      調整や視力測定など、<br>
      無料でさせて頂いておりますので<br>
      お気軽にお申し付け下さい。<br>
      ご来店をお待ちしております。
    </p>

    <section class="shop-card">
      <div class="shop-mark">
        <span class="dot"></span>
        <span class="name">ミハラ</span>
      </div>
      <div class="shop-info">
        <p class="shop-name">メガネのミハラ 北町店</p>
        <p class="address">山浦市北町3丁目108-4</p>
        <p class="tel">
          <svg width="22" height="22" viewBox="0 0 24 24" aria-hidden="true">
            <path fill="#1f1f1f" d="M6.6 10.8a15.1 15.1 0 0 0 6.6 6.6l2.2-2.2a1 1 0 0 1 1-.25 11.4 11.4 0 0 0 3.6.57 1 1 0 0 1 1 1V20a1 1 0 0 1-1 1A17 17 0 0 1 3 4a1 1 0 0 1 1-1h3.5a1 1 0 0 1 1 1c0 1.25.2 2.45.57 3.6a1 1 0 0 1-.25 1z"/>
          </svg>
          TEL 000-123-4567
        </p>
      </div>
    </section>
  </main>
</body>
</html>
```